Executive Coaching Consultancy Website Design

I am setting up an executive coaching consultancy practice, primarily targeting ambitious women (and men of course!) who want to progress to the next level in their careers (late 20's to mid forties in age) or who are returning to work after a career break. I need a simple website that promotes the benefits of my consultancy service, contact details plus other associated information and incorporates social media channels so I can update information and news items on a regular basis. It would be useful to have a design for a Worknest dedicated page too.

This project has been on the back burner for a while due to other commitments, however when I originally decided to set the business up a couple of years ago, I did get a logo and some illustrations for the website designed and produced - which I've uploaded.

The design should convey expertise, understanding, serenity and trust. I am keen it appears stylish and different to many of the other coaching websites that use typical business imagery and are very cluttered. I am targeting individuals who want to invest their own time and money into getting to the next step (as opposed to targeting HR teams in large organisations).

The design should also be responsive so the target audience can easily view it on their phones/tablets.

Initially the information to be conveyed on the website will include:

- How coaching can improve career performance
- The coaching process and what to expect
- Fees
- About us
- Contact details
- A Blog
- Links to useful articles/organisations

etc.

A simple scroll down format would make sense but I will leave it to your best judgement!

Many thanks!!

Reason: Realised it was still the holiday period but am keen to receive prospective designs so I can commission this project quickly. Thanks!

Target Market(s)

28-45 yr old career women

Industry/Entity Type

Business

Number of Pages Required

2 page

Requirements
Must have
• Clean, simple intuitive navigation that can be adapted easily for responsive design purposes
Nice to have
• Area for testimonials
Should not have
• Cluttered information.

```html
<!DOCTYPE html>
<html lang="en">
<head>
<meta charset="utf-8">
<title>Halden Reed Coaching</title>
<link href="https://fonts.googleapis.com/css2?family=Open+Sans:wght@300;400;600&display=swap" rel="stylesheet">
<style>
:root{
  --purple:#5b1a8b;
  --purple-soft:#7a3fa6;
  --teal:#1e9aa3;
  --teal-dark:#167f88;
  --text:#8a8a8a;
  --text-light:#a8a8a8;
  --line:#e2e2e2;
  --btn:#efefef;
  --btn-border:#cfcfcf;
  --icon:#9a9a9a;
  --white:#ffffff;
}
*{box-sizing:border-box;margin:0;padding:0}
html,body{width:780px;height:1200px;overflow:hidden;background:var(--white)}
body{font-family:'Open Sans',sans-serif;color:var(--text);position:relative;font-weight:300}
.abs{position:absolute}

/* top bar */
.topbar{left:0;top:0;width:780px;height:14px;background:var(--purple);color:var(--white);font-size:8px;font-weight:400;text-align:right;padding-right:38px;line-height:14px}

/* header */
.brand{left:60px;top:38px;display:flex;align-items:center;gap:8px}
.brand-dot{width:22px;height:22px;border-radius:50%;background:var(--purple)}
.brand-name{font-size:13px;font-weight:600;color:var(--purple);line-height:1.15;letter-spacing:1px}
.social{top:23px;display:flex;gap:4px;right:60px}
.social span{width:16px;height:16px;border:1.2px solid var(--purple);border-radius:50%;display:block}
.nav{top:48px;right:60px;display:flex;gap:14px;font-size:10.5px;color:var(--text-light);font-weight:400}
.nav a{color:inherit;text-decoration:none;position:relative}
.nav a.active{color:var(--purple)}
.nav a.active::after{content:"";position:absolute;left:0;right:0;bottom:-6px;height:3px;background:var(--purple)}
.search{top:73px;right:60px;display:flex;height:22px}
.search-field{width:104px;border:1px solid #cfcfcf;border-right:none;font-size:9px;color:#b5b5b5;padding:4px 6px;font-weight:400}
.search-btn{width:31px;background:var(--purple);display:flex;align-items:center;justify-content:center;border-radius:0 2px 2px 0}

/* hero */
.hero{left:0;top:102px;width:780px;height:300px;background:linear-gradient(110deg,#5a5a5a 0%,#9c9c9c 30%,#c8c8c8 55%,#8d8d8d 80%,#6c6c6c 100%)}
.hero-title{left:98px;top:212px;font-size:48px;color:var(--white);font-weight:300;letter-spacing:1px;line-height:1}
.hero-sub{left:98px;top:262px;font-size:16px;color:var(--white);font-weight:300;letter-spacing:.5px}
.hero-arrow{top:244px}

/* about */
.section-title{font-size:20px;color:#a0a0a0;font-weight:300;text-align:center}
.about-title{left:0;top:412px;width:780px}
.about-text{left:60px;top:444px;width:660px;font-size:10px;line-height:1.35;text-align:center;font-weight:400;color:#9d9d9d}
.btn{background:var(--btn);border:1px solid var(--btn-border);border-radius:2px;font-size:10px;color:#8d8d8d;font-weight:400;text-align:center;line-height:23px;height:25px;width:62px}
.about-more{left:358px;top:499px}
.divider{left:60px;top:540px;width:660px;height:1px;background:var(--line)}

/* features */
.feature{top:558px;width:150px;text-align:center}
.feature-icon{width:42px;height:42px;border-radius:50%;background:var(--icon);margin:0 auto;display:flex;align-items:center;justify-content:center}
.feature-title{font-size:21px;color:var(--purple-soft);font-weight:300;margin-top:12px;white-space:nowrap}
.feature-text{font-size:10px;line-height:1.4;color:#a0a0a0;font-weight:400;margin-top:8px}
.feature .btn{margin:22px auto 0}

/* band */
.band{left:0;top:800px;width:780px;height:190px;background:linear-gradient(100deg,#9fd6b6 0%,#f0e9b8 30%,#f7f2c8 50%,#c7e6b0 75%,#5fc29a 100%)}
.band-glow{left:150px;top:850px;width:170px;height:130px;border-radius:50%;background:radial-gradient(circle,rgba(240,150,110,.55),rgba(240,150,110,0) 70%)}
.band-title{left:0;top:812px;width:780px;text-align:center;font-size:58px;color:var(--teal);font-weight:300}
.band-email{left:252px;top:902px;width:295px;height:28px;background:rgba(255,255,255,.55);font-size:10px;text-align:center;line-height:28px;color:#7d7d7d;font-weight:400}
.band-send{left:360px;top:944px;width:59px;height:23px;background:var(--teal-dark);color:var(--white);font-size:10px;text-align:center;line-height:23px;font-weight:400;border-radius:2px}

/* news */
.news-title{left:58px;top:1008px;font-size:20px;color:#a0a0a0}
.news-arrows{left:352px;top:1019px;display:flex;gap:2px}
.news-arrows span{width:13px;height:15px;background:#e5e5e5;border:1px solid #d8d8d8;display:flex;align-items:center;justify-content:center}
.news-panel{left:60px;top:1040px;width:324px;height:89px;background:#f0f0f0;border:1px solid #dcdcdc;border-radius:3px}
.news-item{top:1047px;width:150px}
.news-date{position:absolute;left:4px;top:0;width:38px;height:42px;background:var(--white);border:1px solid #dcdcdc;text-align:center;color:var(--purple)}
.news-day{font-size:22px;line-height:28px;font-weight:300}
.news-month{font-size:6px;font-weight:400;color:var(--purple-soft)}
.news-head{position:absolute;left:48px;top:0;width:104px;font-size:8.5px;line-height:1.05;color:var(--purple-soft);font-weight:400}
.news-body{position:absolute;left:48px;top:22px;width:104px;font-size:6.5px;line-height:1.15;color:#8a8a8a;font-weight:400}
.news-btn{position:absolute;left:112px;top:50px;width:40px;height:14px;background:var(--btn);border:1px solid var(--btn-border);font-size:6px;line-height:12px;text-align:center;color:#777;font-weight:400}

/* contact */
.contact-title{left:394px;top:1008px;font-size:20px;color:#a0a0a0}
.field{background:#efefef;border:1px solid #dcdcdc;border-radius:2px;font-size:7px;color:#bdbdbd;padding:4px 6px;font-weight:400}
.field-name{left:397px;top:1039px;width:162px;height:20px}
.field-email{left:560px;top:1039px;width:160px;height:20px}
.field-msg{left:397px;top:1066px;width:323px;height:39px}
.contact-send{left:680px;top:1112px;width:40px;height:15px;background:var(--btn);border:1px solid var(--btn-border);font-size:6px;text-align:center;line-height:13px;color:#777;font-weight:400}

/* footer */
.footer-line{left:0;top:1140px;width:780px;height:2px;background:#e6e6e6}
.footer-nav{left:60px;top:1152px;display:flex;gap:26px;font-size:10px;color:#9a9a9a;font-weight:400}
.footer-copy{left:60px;top:1179px;font-size:7px;color:#b0b0b0;font-weight:400}
.footer-contact{left:558px;top:1150px;font-size:7px;line-height:1.6;color:#b0b0b0;font-weight:400}
.footer-social{left:558px;top:1178px;display:flex;gap:3px}
.footer-social span{width:12px;height:12px;border:1px solid #aaa;border-radius:50%}
.footer-brand{left:668px;top:1158px;display:flex;align-items:center;gap:4px}
.footer-brand .brand-dot{width:10px;height:10px}
.footer-brand .brand-name{font-size:6px;letter-spacing:.5px}
</style>
</head>
<body>

<div class="abs topbar">Complete Address Here | 555.010.2040 | 555.010.3090</div>

<header>
  <div class="abs brand">
    <span class="brand-dot"></span>
    <span class="brand-name">HALDEN REED<br>COACHING</span>
  </div>
  <div class="abs social" aria-label="Social links"><span></span><span></span><span></span></div>
  <nav class="abs nav">
    <a class="active">HOME</a><a>SERVICES</a><a>FEES</a><a>ABOUT</a><a>CONTACT</a><a>NEWS</a>
  </nav>
  <div class="abs search">
    <div class="search-field">Search</div>
    <div class="search-btn">
      <svg width="11" height="11" viewBox="0 0 12 12"><circle cx="5" cy="5" r="3.6" fill="none" stroke="#fff" stroke-width="1.8"/><line x1="7.6" y1="7.6" x2="11" y2="11" stroke="#fff" stroke-width="2"/></svg>
    </div>
  </div>
</header>

<section>
  <div class="abs hero" role="img" aria-label="Black and white photo of a small child's hand resting in an adult's open palm"></div>
  <div class="abs hero-title">WELCOME</div>
  <div class="abs hero-sub">HALDEN REED COACHING</div>
  <svg class="abs hero-arrow" style="left:46px" width="10" height="16" viewBox="0 0 10 16"><polyline points="8,2 2,8 8,14" fill="none" stroke="#fff" stroke-width="1.4"/></svg>
  <svg class="abs hero-arrow" style="left:724px" width="10" height="16" viewBox="0 0 10 16"><polyline points="2,2 8,8 2,14" fill="none" stroke="#fff" stroke-width="1.4"/></svg>
</section>

<section>
  <h2 class="abs section-title about-title">ABOUT US</h2>
  <p class="abs about-text">Lorem ipsum dolor sit amet, consectetur adipiscing elit, sed do eiusmod tempor incididunt ut labore et dolore magna aliqua. Ut enim ad minim veniam, quis nostrud exercitation ullamco laboris nisi ut aliquip ex ea commodo consequat. Duis aute irure dolor in reprehenderit in voluptate velit esse cillum dolore eu fugiat nulla pariatur.</p>
  <div class="abs btn about-more">MORE</div>
  <div class="abs divider"></div>
</section>

<section>
  <div class="abs feature" style="left:55px">
    <div class="feature-icon"><svg width="22" height="22" viewBox="0 0 22 22"><rect x="4" y="3" width="13" height="17" rx="1" fill="#fff"/><rect x="8" y="1.5" width="5" height="3" fill="#fff" stroke="#9a9a9a"/><line x1="7" y1="9" x2="14" y2="9" stroke="#9a9a9a"/><line x1="7" y1="12" x2="14" y2="12" stroke="#9a9a9a"/><circle cx="16" cy="17" r="4" fill="#fff" stroke="#9a9a9a"/><polyline points="14,17 15.5,18.5 18,15.5" fill="none" stroke="#9a9a9a"/></svg></div>
    <h3 class="feature-title">LOREM IPSUM</h3>
    <p class="feature-text">Lorem ipsum dolor sit amet, consectetur adipiscing elit, sed do eiusmod tempor incididunt ut labore et dolore magna aliqua. Ut enim ad minim veniam, quis nostrud exercitation ullamco laboris</p>
    <div class="btn">MORE</div>
  </div>
  <div class="abs feature" style="left:227px">
    <div class="feature-icon"><svg width="22" height="22" viewBox="0 0 22 22"><circle cx="7" cy="5" r="2.5" fill="#fff"/><circle cx="15" cy="5" r="2.5" fill="#fff"/><rect x="4.5" y="9" width="5" height="10" rx="1.5" fill="#fff"/><rect x="12.5" y="9" width="5" height="10" rx="1.5" fill="#fff"/></svg></div>
    <h3 class="feature-title">LOREM IPSUM</h3>
    <p class="feature-text">Lorem ipsum dolor sit amet, consectetur adipiscing elit, sed do eiusmod tempor incididunt ut labore et dolore magna aliqua. Ut enim ad minim veniam, quis nostrud exercitation ullamco laboris</p>
    <div class="btn">MORE</div>
  </div>
  <div class="abs feature" style="left:401px">
    <div class="feature-icon"><svg width="22" height="22" viewBox="0 0 22 22"><path d="M4 6 L18 3 L18 7 Z" fill="#fff"/><circle cx="11" cy="10" r="2.5" fill="#fff"/><rect x="8.5" y="13" width="5" height="8" rx="1.5" fill="#fff"/></svg></div>
    <h3 class="feature-title">LOREM IPSUM</h3>
    <p class="feature-text">Lorem ipsum dolor sit amet, consectetur adipiscing elit, sed do eiusmod tempor incididunt ut labore et dolore magna aliqua. Ut enim ad minim veniam, quis nostrud exercitation ullamco laboris</p>
    <div class="btn">MORE</div>
  </div>
  <div class="abs feature" style="left:575px">
    <div class="feature-icon"><svg width="22" height="22" viewBox="0 0 22 22"><circle cx="11" cy="10" r="5" fill="#fff"/><rect x="9" y="15" width="4" height="3" fill="#fff"/><line x1="11" y1="1" x2="11" y2="3" stroke="#fff"/><line x1="3" y1="10" x2="5" y2="10" stroke="#fff"/><line x1="17" y1="10" x2="19" y2="10" stroke="#fff"/><line x1="5" y1="4" x2="6.5" y2="5.5" stroke="#fff"/><line x1="17" y1="4" x2="15.5" y2="5.5" stroke="#fff"/></svg></div>
    <h3 class="feature-title">LOREM IPSUM</h3>
    <p class="feature-text">Lorem ipsum dolor sit amet, consectetur adipiscing elit, sed do eiusmod tempor incididunt ut labore et dolore magna aliqua. Ut enim ad minim veniam, quis nostrud exercitation ullamco laboris</p>
    <div class="btn">MORE</div>
  </div>
</section>

<section>
  <div class="abs band" role="img" aria-label="Sunlit photo of a woman with arms open, leaning back in a bright green and yellow field"></div>
  <div class="abs band-glow"></div>
  <h2 class="abs band-title">Breathe. Encourage.</h2>
  <div class="abs band-email">Email</div>
  <div class="abs band-send">SEND</div>
</section>

<section>
  <h2 class="abs news-title">LATEST NEWS</h2>
  <div class="abs news-arrows">
    <span><svg width="5" height="8" viewBox="0 0 5 8"><polyline points="4,1 1,4 4,7" fill="none" stroke="#999"/></svg></span>
    <span><svg width="5" height="8" viewBox="0 0 5 8"><polyline points="1,1 4,4 1,7" fill="none" stroke="#999"/></svg></span>
  </div>
  <div class="abs news-panel"></div>
  <article class="abs news-item" style="left:64px">
    <div class="news-date"><div class="news-day">07</div><div class="news-month">OCTOBER</div></div>
    <div class="news-head">LOREM IPSUM DOLOR SIT AMET, CONSECTETUR</div>
    <div class="news-body">Ut enim ad minim veniam, quis nostrud exercitation ullamco laboris nisi ut aliquip ex ea</div>
    <div class="news-btn">CONTINUE</div>
  </article>
  <article class="abs news-item" style="left:226px">
    <div class="news-date"><div class="news-day">04</div><div class="news-month">OCTOBER</div></div>
    <div class="news-head">LOREM IPSUM DOLOR SIT AMET, CONSECTETUR</div>
    <div class="news-body">Ut enim ad minim veniam, quis nostrud exercitation ullamco laboris nisi ut aliquip ex ea</div>
    <div class="news-btn">CONTINUE</div>
  </article>

  <h2 class="abs contact-title">CONTACT US</h2>
  <div class="abs field field-name">Name</div>
  <div class="abs field field-email">Email</div>
  <div class="abs field field-msg">Message</div>
  <div class="abs contact-send">SEND</div>
</section>

<footer>
  <div class="abs footer-line"></div>
  <nav class="abs footer-nav"><span>HOME</span><span>SERVICES</span><span>FEES</span><span>ABOUT</span><span>CONTACT</span><span>BLOG</span></nav>
  <div class="abs footer-copy">© 2014 | Halden Reed Coaching. All Rights Reserved.</div>
  <div class="abs footer-contact">Complete Address Here<br>Phone 555.010.2040</div>
  <div class="abs footer-social"><span></span><span></span><span></span></div>
  <div class="abs footer-brand"><span class="brand-dot"></span><span class="brand-name">HALDEN REED<br>COACHING</span></div>
</footer>

</body>
</html>
```